Letter head incorporating Our values and our Pebble & Fern logo

here are our current letterheads, similar look and feel but incorporating our values logo too.
I have attached some of our flyers to give an idea of our look and feel of our brand

```html
<!DOCTYPE html>
<html lang="en">
<head>
<meta charset="utf-8">
<title>Pebble &amp; Fern Letterhead</title>
<link href="https://fonts.googleapis.com/css2?family=Open+Sans:wght@400;600;700&family=Jost:wght@400;500&display=swap" rel="stylesheet">
<style>
  :root {
    --brand-blue: #1ba3dd;
    --accent-red: #ef3b3b;
    --text-grey: #6b6b6b;
    --text-dark: #3a3a3a;
    --paper: #ffffff;
    --wash-yellow: #fffbe3;
    --wash-green: #f1f8e8;
    --wash-blue: #edf4fb;
  }
  * { margin: 0; padding: 0; box-sizing: border-box; }
  html, body { width: 922px; height: 1200px; overflow: hidden; background: var(--paper); }
  .letterhead {
    position: relative;
    width: 922px;
    height: 1200px;
    background: var(--paper);
    font-family: "Open Sans", sans-serif;
    color: var(--text-grey);
    overflow: hidden;
  }
  .background-art {
    position: absolute;
    left: 300px;
    top: 490px;
    width: 622px;
    height: 710px;
    background:
      radial-gradient(circle 215px at 331px 410px, var(--wash-yellow) 0%, var(--wash-yellow) 80%, rgba(255,251,227,0) 100%),
      radial-gradient(ellipse 90px 150px at 190px 610px, var(--wash-blue) 0%, rgba(237,244,251,0) 100%);
  }
  .brand-flag {
    position: absolute;
    left: 82px;
    top: 0;
    width: 195px;
    height: 237px;
  }
  .brand-flag svg { display: block; }
  .brand-mark {
    position: absolute;
    left: 82px;
    top: 36px;
    width: 32px;
    height: 32px;
    border-radius: 50%;
    background: #ffffff;
  }
  .brand-name {
    position: absolute;
    left: 0;
    top: 90px;
    width: 195px;
    text-align: center;
    font-weight: 700;
    font-size: 23px;
    line-height: 1.15;
    color: #ffffff;
  }
  .school-contacts {
    position: absolute;
    right: 68px;
    top: 54px;
    font-family: "Jost", sans-serif;
    font-size: 13px;
    color: var(--text-grey);
    text-align: right;
  }
  .school-contacts li {
    list-style: none;
    display: flex;
    justify-content: flex-end;
    align-items: center;
    gap: 6px;
    margin-bottom: 8px;
    line-height: 1.2;
  }
  .school-contacts li.address { margin-bottom: 14px; }
  .icon {
    flex: none;
    width: 17px;
    height: 17px;
    border-radius: 3px;
    background: var(--accent-red);
    display: flex;
    align-items: center;
    justify-content: center;
  }
  .sender {
    position: absolute;
    left: 82px;
    top: 281px;
  }
  .sender-name {
    font-size: 24px;
    font-weight: 600;
    color: var(--brand-blue);
    line-height: 1.2;
  }
  .sender-title {
    font-size: 13px;
    color: var(--text-dark);
    margin-top: 4px;
  }
  .sender-details {
    margin-top: 13px;
    font-size: 15.5px;
    color: var(--text-dark);
  }
  .sender-details div { height: 24px; line-height: 24px; }
  .sender-details dt {
    display: inline-block;
    width: 31px;
    color: var(--brand-blue);
    font-weight: 600;
  }
  .sender-details dd { display: inline; }
  .letter-date {
    position: absolute;
    right: 80px;
    top: 420px;
    font-size: 19.5px;
    color: var(--text-dark);
  }
  .letter-body {
    position: absolute;
    left: 82px;
    top: 486px;
    width: 757px;
    font-size: 16.3px;
    line-height: 22.4px;
    text-align: justify;
    color: var(--text-grey);
  }
  .letter-body p + p { margin-top: 22.4px; }
  .signature {
    position: absolute;
    left: 100px;
    top: 852px;
    width: 130px;
    height: 78px;
    border-radius: 6px;
    background: linear-gradient(100deg, rgba(40,40,40,0.02) 0%, rgba(40,40,40,0.07) 50%, rgba(40,40,40,0.02) 100%);
  }
  .signatory {
    position: absolute;
    left: 82px;
    top: 940px;
    font-family: "Jost", sans-serif;
    font-size: 21px;
    font-weight: 500;
    color: var(--text-dark);
  }
</style>
</head>
<body>
<main class="letterhead">
  <div class="background-art" role="img" aria-label="Faint watermark illustration of a sun and a child flying a kite"></div>

  <header>
    <div class="brand-flag">
      <svg width="195" height="237" viewBox="0 0 195 237" aria-hidden="true">
        <polygon points="0,0 195,0 195,237 0,203" fill="#1ba3dd"/>
      </svg>
      <span class="brand-mark" aria-hidden="true"></span>
      <div class="brand-name">Pebble &amp; Fern</div>
    </div>

    <ul class="school-contacts">
      <li class="address">
        <span>27 Wattlebrook Lane<br>ASHGROVE NSW 2031</span>
        <span class="icon"><svg width="11" height="11" viewBox="0 0 12 12"><path d="M6 1a3.6 3.6 0 0 0-3.6 3.6C2.4 7.3 6 11 6 11s3.6-3.7 3.6-6.4A3.6 3.6 0 0 0 6 1zm0 5a1.4 1.4 0 1 1 0-2.8A1.4 1.4 0 0 1 6 6z" fill="#fff"/></svg></span>
      </li>
      <li>
        <span>(02) 5550 3186</span>
        <span class="icon"><svg width="11" height="11" viewBox="0 0 12 12"><path d="M3 1.5l2 2-1 1.3c.6 1.2 1.6 2.2 2.8 2.8l1.3-1 2 2-1.2 1.4C5.6 9.8 2.2 6.4 1.6 3.1z" fill="#fff"/></svg></span>
      </li>
      <li>
        <span>0400 555 219</span>
        <span class="icon"><svg width="11" height="11" viewBox="0 0 12 12"><rect x="3.2" y="1" width="5.6" height="10" rx="1" fill="none" stroke="#fff" stroke-width="1.3"/></svg></span>
      </li>
      <li>
        <span>ashgrove@pebbleandfern.edu.au</span>
        <span class="icon"><svg width="11" height="11" viewBox="0 0 12 12"><rect x="1" y="2.5" width="10" height="7" fill="none" stroke="#fff" stroke-width="1.2"/><path d="M1 2.5l5 4 5-4" fill="none" stroke="#fff" stroke-width="1.2"/></svg></span>
      </li>
      <li>
        <span>pebbleandfern.edu.au</span>
        <span class="icon"><svg width="11" height="11" viewBox="0 0 12 12"><path d="M3 1.5v8.5l2.2-2 1.6 3 1.4-.7-1.6-3h3z" fill="#fff"/></svg></span>
      </li>
    </ul>
  </header>

  <section class="sender">
    <h1 class="sender-name">Daniel Marsh</h1>
    <p class="sender-title">Chief Director</p>
    <dl class="sender-details">
      <div><dt>A :</dt><dd>1120 Harbour Street, Portview 40217</dd></div>
      <div><dt>W :</dt><dd>www.pebbleandfern-school.com</dd></div>
      <div><dt>P :</dt><dd>+00 555 018 42</dd></div>
      <div><dt>M :</dt><dd>office@pebbleandfern-mail.com</dd></div>
    </dl>
  </section>

  <p class="letter-date">12 December, 2025</p>

  <article class="letter-body">
    <p>Lorem ipsum dolor sit amet, consectetuer adipiscing elit, sed diam nonummy nibh euismod tincidunt ut laoreet dolore magna aliquam erat volutpat. Ut wisi enim ad minim veniam, quis nostrud exerci tation ullamcorper suscipit lobortis nisl ut aliquip ex ea commodo consequat. Duis autem vel eum iriure dolor in hendrerit in vulputate velit esse molestie consequat, vel illum dolore eu feugiat nulla facilisis at vero eros et accumsan et iusto odio dignissim qui blandit praesent luptatum zzril delenit augue duis dolore te feugait nulla facilisi.</p>
    <p>Lorem ipsum dolor sit amet, cons ectetuer adipiscing elit, sed diam nonummy nibh euismod tincidunt ut laoreet dolore magna aliquam erat volutpat. Ut wisi enim ad minim veniam, quis nostrud exerci tation ullamcorper suscipit lobortis nisl ut aliquip ex ea commodo consequat.</p>
    <p>Lorem ipsum dolor sit amet, consectetuer adipiscing elit, sed diam nonummy nibh euismod tincidunt ut laoreet dolore magna aliquam eratveniam, quis nostrud exerci tation ullamcorper suscipit lobortis nisl ut aliquip ex ea commodo consequat. Lorem ipsum dolor sit zamet, consectetuer adipiscing elit, sed diam nonummy nibh euismod tincidunt.</p>
  </article>

  <div class="signature" role="img" aria-label="Handwritten signature"></div>
  <p class="signatory">Mr. Daniel Marsh</p>
</main>
</body>
</html>
```